Business Card for Quillmark Ledger - A cannabis publication for executives.

I'd like some business cards for Quillmark Ledger. The logo is done (great job!) and I need a card design I will use with PRINTLY. I made it a short project to allow time for printing before an event. These will be standard sized cards (final artwork size 3.66" x 2.16" at 300dpi) with a final card size of 3.5" x 2.0". (See PRINTLY.com if you need more info.) I might try rounded corners but am not sure yet. I think the design will work okay with rounded.

Quillmark Ledger will be a bi-weekly publication for the cannabis industry. It is targeted to investors and industry executives, not consumers or pot smokers. So our market is more B2B. However I am open to creativity and making the card something people remark on.

My contact for card:

Dana Merrow
Founder/CEO
dana@quillmarkledger.example

2740 Harlow Avenue
Boston MA 02135
(617)555-0194

Target Market(s)

Executives, Industry people and investors in the Cannabis sector.

Contact Information for Business Card

PRINTLY does do double sided and the second side can be the same or different images. Only one side is required but use of the second side would be a bonus.

Font styles to use
Serif
Sans Serif
Decorative

Colors

Designer to choose colors to be used in the design.

Requirements
Must have
• Logo, contact info
Nice to have
• Style and design to make the card stand out in a crowd.

```html
<!DOCTYPE html>
<html lang="en">
<head>
<meta charset="utf-8">
<title>Quillmark Ledger — Business Card</title>
<link href="https://fonts.googleapis.com/css2?family=Montserrat:wght@400;500;700&display=swap" rel="stylesheet">
<style>
  :root {
    --brand-blue: #1d75bf;
    --brand-green: #72ad2f;
    --paper: #ffffff;
    --ink-dark: #2b2b2b;
    --backdrop: #5c6266;
  }
  * { margin: 0; padding: 0; box-sizing: border-box; }
  html, body { width: 1200px; height: 900px; overflow: hidden; }
  body {
    background: var(--backdrop);
    font-family: "Montserrat", Arial, sans-serif;
    display: flex;
    align-items: center;
    justify-content: center;
    gap: 40px;
  }
  .card {
    position: relative;
    width: 540px;
    height: 309px;
    border-radius: 18px;
    overflow: hidden;
    box-shadow: 0 10px 24px rgba(0,0,0,0.35);
  }

  /* Front */
  .card-front { background: var(--paper); }
  .front-art { position: absolute; inset: 0; }
  .wordmark {
    position: absolute;
    display: flex;
    align-items: center;
    gap: 10px;
    font-weight: 700;
    white-space: nowrap;
  }
  .card-front .wordmark { left: 34px; top: 44px; font-size: 26px; color: var(--brand-blue); }
  .wordmark-square { width: 22px; height: 22px; background: var(--brand-green); }
  .holder {
    position: absolute;
    right: 40px;
    top: 96px;
    text-align: right;
  }
  .holder-name { font-size: 19px; font-weight: 700; color: var(--brand-blue); }
  .holder-title {
    font-size: 12px;
    font-weight: 400;
    color: var(--ink-dark);
    padding-bottom: 5px;
    border-bottom: 2px solid var(--brand-blue);
    display: inline-block;
  }
  .contact-list {
    position: absolute;
    left: 222px;
    top: 182px;
    list-style: none;
    color: var(--paper);
    font-size: 11.5px;
    font-weight: 400;
    line-height: 1.25;
  }
  .contact-item { display: flex; align-items: center; gap: 12px; margin-bottom: 8px; }
  .contact-icon {
    width: 20px; height: 20px;
    background: var(--paper);
    border-radius: 4px;
    display: flex; align-items: center; justify-content: center;
    flex-shrink: 0;
  }

  /* Back */
  .card-back {
    background: var(--brand-blue);
    display: flex;
    align-items: center;
    justify-content: center;
  }
  .card-back .wordmark { position: static; font-size: 38px; color: var(--paper); gap: 14px; }
  .card-back .wordmark-square { width: 32px; height: 32px; background: var(--paper); }
</style>
</head>
<body>

  <section class="card card-front" aria-label="Card front">
    <svg class="front-art" width="540" height="309" viewBox="0 0 540 309" aria-hidden="true">
      <polygon class="accent-wedge" points="228,152 240,152 160,286 142,286 142,236" fill="var(--brand-green)"/>
      <polygon class="contact-panel" points="236,158 510,158 510,286 156,286" fill="var(--brand-blue)"/>
    </svg>

    <div class="wordmark"><span class="wordmark-square"></span>Quillmark Ledger</div>

    <div class="holder">
      <div class="holder-name">Dana Merrow</div>
      <div class="holder-title">Founder/CEO</div>
    </div>

    <ul class="contact-list">
      <li class="contact-item">
        <span class="contact-icon">
          <svg width="12" height="12" viewBox="0 0 24 24"><path fill="var(--brand-blue)" d="M6.6 10.8a15 15 0 0 0 6.6 6.6l2.2-2.2c.3-.3.7-.4 1-.2 1.1.4 2.3.6 3.6.6.6 0 1 .4 1 1V20c0 .6-.4 1-1 1A17 17 0 0 1 3 4c0-.6.4-1 1-1h3.5c.6 0 1 .4 1 1 0 1.3.2 2.5.6 3.6.1.3 0 .7-.2 1z"/></svg>
        </span>
        (617)555-0194
      </li>
      <li class="contact-item">
        <span class="contact-icon">
          <svg width="12" height="12" viewBox="0 0 24 24" fill="none" stroke="var(--brand-blue)" stroke-width="3" stroke-linecap="round"><path d="M10 14a4 4 0 0 0 5.7 0l3-3a4 4 0 0 0-5.7-5.7l-1 1"/><path d="M14 10a4 4 0 0 0-5.7 0l-3 3a4 4 0 0 0 5.7 5.7l1-1"/></svg>
        </span>
        dana@quillmarkledger.example
      </li>
      <li class="contact-item">
        <span class="contact-icon">
          <svg width="12" height="12" viewBox="0 0 24 24"><path fill="var(--brand-blue)" d="M12 2a7 7 0 0 0-7 7c0 5 7 13 7 13s7-8 7-13a7 7 0 0 0-7-7zm0 9.5A2.5 2.5 0 1 1 12 6.5a2.5 2.5 0 0 1 0 5z"/></svg>
        </span>
        <span>2740 Harlow Avenue<br>Boston MA 02135</span>
      </li>
    </ul>
  </section>

  <section class="card card-back" aria-label="Card back">
    <div class="wordmark"><span class="wordmark-square"></span>Quillmark Ledger</div>
  </section>

</body>
</html>
```